Business Card Design

Melodrift Podcast

Industry/Entity Type

Business

Contact Information for Business Card

YOU ARE INVITED TO LISTEN
Stretch Your Mindset
Award Winning Melodrift Podcast
with Dr. Maren Holloway
www.drmarenholloway.example

555-781-3096

```html
<!DOCTYPE html>
<html lang="en">
<head>
<meta charset="utf-8">
<title>Dr. Maren Holloway – Business Card</title>
<link rel="stylesheet" href="https://fonts.googleapis.com/css2?family=Noto+Serif:wght@400&family=Open+Sans:wght@400&display=swap">
<style>
  :root {
    --page-bg: #ecebe6;
    --card-light: #c3df84;
    --card-mid: #aed066;
    --card-dark: #94bd48;
    --pill: #86ad3c;
    --pill-text: #f3f7e8;
    --ink: #1f2a12;
    --ink-soft: #3d5220;
    --icon: #2f7a33;
    --mic-light: #e4e6e8;
    --mic-mid: #a9adb2;
    --mic-dark: #5d6166;
  }
  * { margin: 0; padding: 0; box-sizing: border-box; }
  html, body { width: 1200px; height: 1200px; overflow: hidden; background: var(--page-bg); }
  .canvas {
    width: 1200px; height: 1200px;
    display: flex; flex-direction: column; align-items: center; justify-content: center; gap: 40px;
  }
  .card {
    position: relative;
    width: 960px; height: 548px;
    overflow: hidden;
    background: radial-gradient(ellipse at 35% 40%, var(--card-light) 0%, var(--card-mid) 55%, var(--card-dark) 100%);
    box-shadow: 0 6px 18px rgba(0,0,0,0.18);
  }
  .name-pill {
    position: absolute; left: 0; top: 150px;
    width: 500px; height: 92px;
    background: var(--pill);
    border-radius: 0 46px 46px 0;
    display: flex; align-items: center; padding-left: 44px;
  }
  .name {
    font-family: "Noto Serif", Georgia, serif;
    font-size: 38px; color: var(--pill-text); white-space: nowrap;
  }
  .contact {
    position: absolute;
    font-family: "Open Sans", Arial, sans-serif;
    font-size: 28px; color: var(--ink);
    display: flex; flex-direction: column; gap: 14px;
  }
  .contact-line { display: flex; align-items: center; gap: 16px; white-space: nowrap; }
  .contact-line svg { width: 26px; height: 26px; flex: none; }
  .card--front .contact { left: 70px; top: 380px; }
  .card--back .contact { left: 70px; top: 330px; font-size: 26px; }
  .invitation {
    position: absolute; left: 70px; top: 60px;
    display: flex; flex-direction: column; gap: 10px;
    white-space: nowrap;
  }
  .invite {
    font-family: "Open Sans", Arial, sans-serif;
    font-size: 20px; letter-spacing: 3px; color: var(--ink-soft);
  }
  .tagline {
    font-family: "Noto Serif", Georgia, serif;
    font-size: 40px; color: var(--ink);
  }
  .podcast {
    font-family: "Open Sans", Arial, sans-serif;
    font-size: 26px; color: var(--ink);
  }
  .host {
    font-family: "Noto Serif", Georgia, serif;
    font-size: 24px; color: var(--ink-soft);
  }
  .mic-photo {
    position: absolute;
    border-radius: 46% 46% 40% 40%;
    background: radial-gradient(ellipse at 40% 35%, var(--mic-light) 0%, var(--mic-mid) 55%, var(--mic-dark) 100%);
  }
  .card--front .mic-photo { left: 540px; top: -40px; width: 340px; height: 470px; }
  .card--back .mic-photo { left: 660px; top: 20px; width: 260px; height: 560px; }
</style>
</head>
<body>
<main class="canvas">
  <section class="card card--front">
    <div class="mic-photo" role="img" aria-label="Photograph of a chrome vintage studio microphone"></div>
    <div class="name-pill"><span class="name">Dr. Maren Holloway</span></div>
    <div class="contact">
      <div class="contact-line">
        <svg viewBox="0 0 24 24" aria-hidden="true"><path fill="var(--icon)" d="M6.6 10.8a15.1 15.1 0 0 0 6.6 6.6l2.2-2.2a1 1 0 0 1 1-.25 11.4 11.4 0 0 0 3.6.57 1 1 0 0 1 1 1V20a1 1 0 0 1-1 1A17 17 0 0 1 3 4a1 1 0 0 1 1-1h3.5a1 1 0 0 1 1 1c0 1.25.2 2.45.57 3.6a1 1 0 0 1-.25 1z"/></svg>
        <span>555-781-3096</span>
      </div>
      <div class="contact-line">
        <svg viewBox="0 0 24 24" aria-hidden="true"><g fill="none" stroke="var(--icon)" stroke-width="2"><circle cx="12" cy="12" r="9"/><ellipse cx="12" cy="12" rx="4" ry="9"/><path d="M3 12h18M5 7h14M5 17h14"/></g></svg>
        <span>www.drmarenholloway.example</span>
      </div>
    </div>
  </section>

  <section class="card card--back">
    <div class="mic-photo" role="img" aria-label="Photograph of a chrome vintage studio microphone"></div>
    <div class="invitation">
      <p class="invite">YOU ARE INVITED TO LISTEN</p>
      <p class="tagline">Stretch Your Mindset</p>
      <p class="podcast">Award Winning Melodrift Podcast</p>
      <p class="host">with Dr. Maren Holloway</p>
    </div>
    <div class="contact">
      <div class="contact-line">
        <svg viewBox="0 0 24 24" aria-hidden="true"><path fill="var(--icon)" d="M6.6 10.8a15.1 15.1 0 0 0 6.6 6.6l2.2-2.2a1 1 0 0 1 1-.25 11.4 11.4 0 0 0 3.6.57 1 1 0 0 1 1 1V20a1 1 0 0 1-1 1A17 17 0 0 1 3 4a1 1 0 0 1 1-1h3.5a1 1 0 0 1 1 1c0 1.25.2 2.45.57 3.6a1 1 0 0 1-.25 1z"/></svg>
        <span>555-781-3096</span>
      </div>
      <div class="contact-line">
        <svg viewBox="0 0 24 24" aria-hidden="true"><g fill="none" stroke="var(--icon)" stroke-width="2"><circle cx="12" cy="12" r="9"/><ellipse cx="12" cy="12" rx="4" ry="9"/><path d="M3 12h18M5 7h14M5 17h14"/></g></svg>
        <span>www.drmarenholloway.example</span>
      </div>
    </div>
  </section>
</main>
</body>
</html>
```